eCommerce website for the sale of vehicle tyres

We need the design of a logo and website for an ecommerce website that sells tyres to vehicle owners.

Users to the website should be able to search brand of tyre, type of tyre and make payment online.

The website should have algorithm to calculate delivery price based on user location and include in total price payable by CoinLark or SwiftTill.

Multi-language website (5 languages)
Content for website available in attached brief.

Number of pages:
1. Home page (with slider on how it works and search area)
2. Search results page
3. About Us page
4. Contact Us page

Target Market(s)

Owners of vehicles

Industry/Entity Type

Automotive

Logo Text

Vorel

Coding

Coded - Design and coding required

Number of Pages Required

5+ page

Font styles to use
Serif

Colors
0255a3
9d9d9d
ec1f27

Requirements
Must have
• Clean design
• Search feature on front page
Should not have
• Complicated

```html
<!DOCTYPE html>
<html lang="en">
<head>
<meta charset="utf-8">
<title>Vorel — Best Tyres at the Best Prices</title>
<link href="https://fonts.googleapis.com/css2?family=Raleway:wght@400;500;600;700&family=Open+Sans:wght@400;600;700&display=swap" rel="stylesheet">
<style>
  :root {
    --blue: #0255a3;
    --blue-dark: #01427f;
    --red: #ec1f27;
    --red-dark: #b8141b;
    --grey: #9d9d9d;
    --grey-light: #eeeeee;
    --ink: #333333;
    --white: #ffffff;
  }
  * { box-sizing: border-box; margin: 0; padding: 0; }
  html, body { width: 896px; height: 1200px; overflow: hidden; }
  body { font-family: "Open Sans", Arial, sans-serif; color: var(--ink); background: var(--white); position: relative; }

  /* Header */
  .site-header { position: absolute; top: 0; left: 0; width: 896px; height: 96px; }
  .brand { position: absolute; left: 136px; top: 8px; }
  .brand-name { font-family: "Raleway", sans-serif; font-weight: 700; font-size: 38px; line-height: 40px; color: var(--ink); letter-spacing: -0.5px; }
  .brand-tagline { font-size: 8px; font-weight: 700; color: var(--red); letter-spacing: 0.6px; margin-top: 2px; }
  .utility { position: absolute; right: 136px; top: 12px; display: flex; align-items: center; gap: 8px; font-size: 9px; color: #666; }
  .utility .sep { color: #bbb; }
  .cart { width: 16px; height: 14px; }
  .language { position: absolute; right: 136px; top: 34px; border: 1px solid #ccc; font-size: 8px; padding: 3px 6px; display: flex; gap: 5px; align-items: center; color: #555; }
  .language .flag { width: 10px; height: 7px; background: var(--blue); border: 1px solid var(--red); }

  /* Navigation */
  .main-nav { position: absolute; top: 96px; left: 0; width: 896px; height: 24px; background: var(--blue); }
  .main-nav ul { list-style: none; display: flex; margin-left: 190px; height: 24px; }
  .main-nav li { font-family: "Raleway", sans-serif; font-size: 10px; font-weight: 600; color: var(--white); padding: 0 20px; line-height: 24px; }
  .main-nav li.active { background: var(--blue-dark); }

  /* Hero slider */
  .hero { position: absolute; top: 120px; left: 0; width: 896px; height: 318px; background: linear-gradient(180deg, #4d5a68 0%, #6f7985 45%, #3f4852 100%); }
  .hero-steps { position: absolute; top: 40px; left: 146px; width: 604px; display: flex; justify-content: space-between; }
  .step { width: 170px; text-align: center; color: var(--white); }
  .step-photo { width: 132px; height: 132px; border-radius: 50%; border: 5px solid var(--white); margin: 0 auto; background: radial-gradient(circle, #d5d9de 0%, #8a9099 60%, #3d434b 100%); }
  .step h3 { font-family: "Raleway", sans-serif; font-size: 11px; font-weight: 600; margin-top: 10px; line-height: 14px; }
  .step p { font-size: 7px; line-height: 10px; margin-top: 4px; color: #e4e6e9; }
  .hero-arrow { position: absolute; top: 96px; width: 22px; height: 40px; }
  .slider-dots { position: absolute; bottom: 14px; left: 0; width: 100%; display: flex; justify-content: center; gap: 6px; }
  .slider-dots span { width: 7px; height: 7px; border-radius: 50%; background: rgba(255,255,255,0.55); }
  .slider-dots span.on { background: var(--white); }

  /* Search */
  .tyre-search { position: absolute; top: 438px; left: 0; width: 896px; height: 76px; background: var(--grey-light); padding: 12px 150px 0; }
  .tyre-search h2 { font-family: "Raleway", sans-serif; font-size: 14px; font-weight: 600; color: var(--ink); }
  .search-row { display: flex; gap: 12px; margin-top: 10px; }
  .select { width: 118px; height: 18px; background: var(--white); border: 1px solid #ccc; font-size: 7px; color: #888; padding: 0 6px; display: flex; justify-content: space-between; align-items: center; }
  .search-btn { width: 58px; height: 18px; background: var(--red); color: var(--white); font-size: 8px; font-weight: 700; text-align: center; line-height: 18px; }

  /* About */
  .about { position: absolute; top: 546px; left: 150px; width: 596px; text-align: center; }
  .section-title { font-family: "Raleway", sans-serif; font-size: 19px; font-weight: 600; color: var(--ink); letter-spacing: 0.5px; }
  .section-rule { width: 60px; height: 2px; background: var(--grey); margin: 6px auto 0; }
  .about p { font-size: 8px; line-height: 12px; color: #666; margin-top: 12px; }

  /* Featured products */
  .featured { position: absolute; top: 712px; left: 0; width: 896px; text-align: center; }
  .featured .section-title { color: var(--blue); }
  .products { position: absolute; top: 48px; left: 150px; display: flex; gap: 12px; }
  .product { width: 140px; height: 196px; background: var(--white); border: 1px solid #ddd; text-align: left; }
  .product-photo { width: 128px; height: 110px; margin: 6px auto 0; background: radial-gradient(circle, #f4f4f4 0%, #9a9a9a 45%, #2b2b2b 62%, #ffffff 64%); }
  .product h4 { font-size: 9px; font-weight: 700; margin: 8px 8px 0; }
  .product small { display: block; font-size: 6.5px; color: #888; margin: 2px 8px 0; line-height: 9px; }
  .product-foot { display: flex; justify-content: space-between; align-items: center; margin: 10px 8px 0; }
  .price { font-size: 11px; font-weight: 700; color: var(--blue); }
  .add-cart { background: var(--blue); color: var(--white); font-size: 7px; padding: 3px 7px; }
  .carousel-arrow { position: absolute; top: 120px; width: 14px; height: 28px; }

  /* Footer */
  .site-footer { position: absolute; top: 1012px; left: 0; width: 896px; height: 146px; background: var(--red); color: var(--white); padding: 20px 150px 0; display: flex; gap: 42px; }
  .footer-col h5 { font-family: "Raleway", sans-serif; font-size: 10px; font-weight: 700; margin-bottom: 6px; }
  .footer-col ul { list-style: none; }
  .footer-col li { font-size: 7.5px; line-height: 12px; }
  .footer-col.contact { width: 180px; }
  .payments { display: flex; gap: 6px; margin-top: 6px; }
  .payments span { background: var(--white); color: var(--ink); font-size: 7px; font-weight: 600; padding: 2px 6px; }
  .footer-bottom { position: absolute; top: 1158px; left: 0; width: 896px; height: 42px; background: var(--red-dark); color: #f5cccc; font-size: 7px; padding: 0 150px; display: flex; justify-content: space-between; align-items: center; }
  .social { display: flex; gap: 5px; }
  .social span { width: 12px; height: 12px; background: var(--white); }
</style>
</head>
<body>

<header class="site-header">
  <div class="brand">
    <div class="brand-name">Vorel</div>
    <div class="brand-tagline">BEST TYRES AT THE BEST PRICES</div>
  </div>
  <nav class="utility">
    <span>My Account</span><span class="sep">|</span>
    <span>Wishlist</span><span class="sep">|</span>
    <span>Sign up</span><span class="sep">|</span>
    <span>Checkout</span>
    <svg class="cart" viewBox="0 0 16 14"><path d="M0 1h3l2 8h8l2-6H4" fill="none" stroke="#0255a3" stroke-width="1.6"/><circle cx="6" cy="12" r="1.4" fill="#0255a3"/><circle cx="12" cy="12" r="1.4" fill="#0255a3"/></svg>
  </nav>
  <div class="language"><span class="flag"></span>English<span>▾</span></div>
</header>

<nav class="main-nav">
  <ul>
    <li class="active">HOME</li>
    <li>ABOUT US</li>
    <li>SEARCH</li>
    <li>CONTACT US</li>
  </ul>
</nav>

<section class="hero" role="img" aria-label="Tyre warehouse with stacked tyres in the background">
  <div class="hero-steps">
    <div class="step">
      <div class="step-photo" role="img" aria-label="Close-up of a tyre on a wheel"></div>
      <h3>Search your tyre by Tyre Size</h3>
      <p>Choose width, profile and rim size to see every tyre that fits your vehicle today.</p>
    </div>
    <div class="step">
      <div class="step-photo" role="img" aria-label="Hands typing on a laptop"></div>
      <h3>Place your order online</h3>
      <p>Add tyres to your cart and pay securely online with the method of your choice.</p>
    </div>
    <div class="step">
      <div class="step-photo" role="img" aria-label="Delivery van on the road"></div>
      <h3>We deliver your tyre at your home or garage of your choice for fitting</h3>
      <p>Delivery cost is worked out for your area and added to your total.</p>
    </div>
  </div>
  <svg class="hero-arrow" style="left:322px" viewBox="0 0 22 40"><path d="M3 3l16 17L3 37" fill="none" stroke="#fff" stroke-width="4"/></svg>
  <svg class="hero-arrow" style="left:539px" viewBox="0 0 22 40"><path d="M3 3l16 17L3 37" fill="none" stroke="#fff" stroke-width="4"/></svg>
  <div class="slider-dots"><span class="on"></span><span></span><span></span><span></span></div>
</section>

<section class="tyre-search">
  <h2>Search Your Tyre</h2>
  <div class="search-row">
    <div class="select">Select Width<span>▾</span></div>
    <div class="select">Select Profile<span>▾</span></div>
    <div class="select">Select Rim<span>▾</span></div>
    <div class="select">Select Brand<span>▾</span></div>
    <div class="search-btn">SEARCH</div>
  </div>
</section>

<section class="about">
  <h2 class="section-title">ABOUT OUR COMPANY</h2>
  <div class="section-rule"></div>
  <p>We provide our customers with the best tyres at the best prices. We are a team of tyre specialists who source quality brands directly from trusted suppliers and pass the savings on to you. Search by size or brand, order online and we deliver to your home or to the garage of your choice, wherever you are in the country.</p>
</section>

<section class="featured">
  <h2 class="section-title">FEATURED PRODUCTS</h2>
  <div class="section-rule"></div>
  <svg class="carousel-arrow" style="left:118px" viewBox="0 0 14 28"><path d="M12 2L2 14l10 12" fill="none" stroke="#9d9d9d" stroke-width="2.5"/></svg>
  <div class="products">
    <article class="product">
      <div class="product-photo" role="img" aria-label="Tyre on alloy wheel"></div>
      <h4>Product Name</h4>
      <small>Short product detail line here for size</small>
      <div class="product-foot"><span class="price">R17.58</span><span class="add-cart">Add to Cart</span></div>
    </article>
    <article class="product">
      <div class="product-photo" role="img" aria-label="Tyre on alloy wheel"></div>
      <h4>Product Name</h4>
      <small>Short product detail line here for size</small>
      <div class="product-foot"><span class="price">R17.58</span><span class="add-cart">Add to Cart</span></div>
    </article>
    <article class="product">
      <div class="product-photo" role="img" aria-label="Tyre on alloy wheel"></div>
      <h4>Product Name</h4>
      <small>Short product detail line here for size</small>
      <div class="product-foot"><span class="price">R17.58</span><span class="add-cart">Add to Cart</span></div>
    </article>
    <article class="product">
      <div class="product-photo" role="img" aria-label="Tyre on alloy wheel"></div>
      <h4>Product Name</h4>
      <small>Short product detail line here for size</small>
      <div class="product-foot"><span class="price">R17.58</span><span class="add-cart">Add to Cart</span></div>
    </article>
  </div>
  <svg class="carousel-arrow" style="left:764px" viewBox="0 0 14 28"><path d="M2 2l10 12L2 26" fill="none" stroke="#9d9d9d" stroke-width="2.5"/></svg>
</section>

<footer class="site-footer">
  <div class="footer-col">
    <h5>COMPANY</h5>
    <ul><li>About Us</li><li>Why Vorel?</li><li>Order Now</li><li>Testimonials</li><li>Best Sellers</li></ul>
  </div>
  <div class="footer-col">
    <h5>PRODUCTS</h5>
    <ul><li>Shipping and Delivery</li><li>Returns &amp; Refunds</li><li>Tyre Size</li><li>Wheels</li><li>Sitemap</li></ul>
  </div>
  <div class="footer-col">
    <h5>SUPPORT</h5>
    <ul><li>FAQ</li><li>Privacy Policy</li><li>Terms &amp; Conditions</li><li>Help Desk</li></ul>
  </div>
  <div class="footer-col contact">
    <h5>CONTACT INFO</h5>
    <ul>
      <li><strong>Kestrel Trading Services</strong></li>
      <li>14 Harbour Road, Fernvale 2194</li>
      <li>Tel: 010 555 0182</li>
      <li>hello@vorel.co.za</li>
    </ul>
    <div class="payments"><span>CoinLark</span><span>SwiftTill</span></div>
  </div>
</footer>

<div class="footer-bottom">
  <span>© 2024 Vorel. All rights reserved.</span>
  <div class="social"><span></span><span></span><span></span><span></span></div>
</div>

</body>
</html>
```